Energy and Environment Venture Capital Blog

Look for an out of the box creative design!

I am working on putting together a new blog / website with a few colleagues in the cleantech / energy venture capital space. I would like to push the box on design and get really creative for how to display the following (very simple):

1) Updated News on venture capital and cleantech (rss feed)
2) Would also like to have a profile page to feature "company of the month"
2.1) Included in this page I would like to be able to have a gallery of photos and have it be an interactive profile of company that includes:
2.1.1) Funding received to date, funders, location, founders (really good example of this is would be on greenledgerhub.com. (there may even be a way to take the date right from their website)
EXTRA: would be amazing to be able to place all the selected company on a map
3) Blog entries that can include photos and movies and active commenting
4) Resources section for interesting websites, books, surveys etc. (pageharbor)
5) Would like to be able to link my social media (chirpline, friendwall)

A couple good examples include:

http://www.moslantic.co.uk/
http://www.copperwindmade.co.uk/
http://www.tarvel-nook.com/

Note: I have a logo designed for the website that I can send across. I also have a domain name registered at http://q7fundloft.com/

I have also attached the draft logo to show the colors I am hoping to use across the site.
Updates

Project Deadline Extended
Reason: Really want to make sure that we get the design right and dont want to have to rush things. If however I find a design concept I like I am happy to pull the trigger right away and work outside the contest.

Target Market(s)

venture capitalists, technologists, SMEs

Industry/Entity Type

Venture Capital

Requirements
Must have
• A funky and creative landing page
The profile page (I would like it to be called Q7 Profiles) should be the feature section of the website
Nice to have
• What I was hoping to do (if possible) was to create a stock index that tracks some of the leading cleantech stocks on the market. Done know if there is anything out there that is open source but if there is I would love a section on the blog called "Q7 Index"
Should not have
• The design should not use old-style, serif fonts like Times New Roman.

```html
<!DOCTYPE html>
<html lang="en">
<head>
<meta charset="utf-8">
<title>Tidewell</title>
<link rel="stylesheet" href="https://fonts.googleapis.com/css2?family=Arimo:ital,wght@0,400;0,700;1,400&family=Open+Sans:wght@400&display=swap">
<style>
:root{
  --ink:#333;
  --muted:#777;
  --rule:#d4d4d4;
  --card-border:#cfcfcf;
  --link:#2a9fd8;
  --green:#6bab1f;
  --red:#d51f1f;
  --up:#3a8a12;
  --quote:#1e5aa8;
  --footer:#b3b3b3;
  --skyline:#e3e3e3;
}
*{box-sizing:border-box;margin:0;padding:0}
html,body{width:1200px;height:822px;overflow:hidden;background:#fff}
body{position:relative;font-family:Arimo,Arial,sans-serif;color:var(--ink)}
.abs{position:absolute}
a{color:var(--link);text-decoration:none;font-weight:700}

.skyline{left:188px;top:0;width:342px;height:66px;background:linear-gradient(180deg,#f4f4f4,var(--skyline))}
.header-rule{left:0;top:66px;width:1200px;height:1px;background:var(--rule)}
.logo-tab{left:312px;top:40px;width:175px;height:58px;background:#fff;border:1px solid var(--rule);border-bottom:none}
.brand{left:326px;top:57px;font-size:28px;font-weight:400;color:#444;display:flex;align-items:center;gap:7px;white-space:nowrap}
.brand-mark{width:24px;height:24px;border:3px solid #444;border-radius:3px}
.tagline{left:316px;top:94px;font-size:7px;font-style:italic;color:var(--muted);white-space:nowrap}

.social-top{left:843px;top:28px;display:flex;gap:4px}
.social-top span{width:10px;height:10px;background:var(--green);border-radius:1px}

.nav{left:542px;top:71px;display:flex;align-items:center;font-size:9px;font-weight:700;color:var(--ink);white-space:nowrap}
.nav li{list-style:none;display:flex;align-items:center;gap:6px}
.nav .ico{width:15px;height:13px;border:2px solid #555;border-radius:2px}

.ticker-rule{left:317px;top:115px;width:566px;height:2px;background:#e6e6e6}
.regions{left:318px;top:125px;width:54px}
.regions li{list-style:none;height:11px;margin-bottom:1px;font-size:6px;font-weight:700;color:#444;padding:2px 0 0 3px;background:linear-gradient(#f7f7f7,#e1e1e1);border:1px solid #c8c8c8}
.regions li.on{background:#fff;width:60px}
.quotes{left:376px;top:123px;width:510px;height:50px}
.quote{position:absolute;top:0;font-size:7.5px;line-height:8.5px;white-space:nowrap}
.quote b{color:var(--quote);font-weight:400;display:block}
.quote .val{color:#111}
.quote .dn{color:var(--red)}
.quote .upc{color:var(--up)}
.quote-bar{position:absolute;top:47px;height:2px;background:var(--red)}
.quote-bar.up{background:var(--green)}
.more{left:865px;top:174px;font-size:5.5px;color:var(--link)}

.card{position:absolute;width:279px;height:255px;border:2px solid var(--card-border);background:#fff}
.card h2{position:absolute;top:16px;font-size:18px;font-weight:700;color:#333;white-space:nowrap}
.dots{position:absolute;top:18px;display:flex;gap:2px}
.dots i{width:8px;height:8px;border-radius:50%;border:1px solid #aaa}
.dots i.on{background:var(--green);border-color:var(--green)}
.card-link{position:absolute;font-size:7.5px;white-space:nowrap}

.news{left:22px;top:45px;width:236px;font-size:7.4px;line-height:11px;color:#444}
.news dt{font-weight:700;color:#333;margin-top:5px}
.news dt:first-child{margin-top:0}

.com-photo{position:absolute;left:22px;top:47px;width:230px;height:98px;background:linear-gradient(90deg,#2e4f74 0%,#4c6f93 40%,#b9bfc6 60%,#7e868f 100%)}
.com-text{position:absolute;left:22px;top:159px;width:236px;font-size:7.4px;line-height:11px;color:#444}

.post{position:absolute;left:20px;width:240px}
.post-head{display:flex;align-items:center;font-size:7px;font-weight:700;white-space:nowrap}
.post-head .av{width:22px;height:18px;border:1px solid #999;border-radius:2px;margin-right:6px}
.post-head small{font-size:5px;font-weight:400;margin-left:2px}
.post-head .time{margin-left:auto;font-size:5px;font-weight:400}
.post-photo{position:absolute;left:0;top:26px;width:83px;height:44px;border:1px solid #ddd}
.post-body{position:absolute;left:88px;top:27px;width:150px;font-size:5.5px;line-height:8px}
.post-meta{position:absolute;left:88px;top:59px;width:150px;font-size:5.5px;display:flex;align-items:center;gap:10px}
.post-meta .count{border:1px solid #999;padding:1px 3px;font-size:5px}
.post-meta .all{margin-left:auto}

.read{position:absolute;left:17px;width:245px}
.read-photo{position:absolute;left:0;top:0;width:74px;height:68px;border:1px solid #ddd}
.read h3{position:absolute;left:82px;top:1px;font-size:7px;font-weight:700}
.read p{position:absolute;left:82px;top:14px;width:165px;font-size:5.5px;line-height:7.5px;color:#444}
.read .see{position:absolute;right:0;top:62px;font-size:5.5px;font-weight:400}

.footer{left:0;top:728px;width:1200px;height:94px;background:var(--footer)}
.footer-nav{position:absolute;left:318px;top:13px;display:flex;gap:11px;font-family:"Open Sans",Arial,sans-serif;font-size:7px;color:#fff;white-space:nowrap}
.follow{position:absolute;left:822px;top:14px;font-family:"Open Sans",Arial,sans-serif;font-size:6.5px;color:#fff}
.social-foot{position:absolute;left:822px;top:27px;display:flex;gap:3px}
.social-foot span{width:10px;height:10px;background:#fff;border-radius:1px}
.footer-brand{position:absolute;left:553px;top:52px;font-size:22px;color:#444;display:flex;align-items:center;gap:6px;white-space:nowrap}
.footer-brand .brand-mark{width:19px;height:19px;border-width:2px}
</style>
</head>
<body>

<div class="abs skyline" role="img" aria-label="Pale grey city skyline silhouette"></div>
<div class="abs header-rule"></div>
<div class="abs logo-tab"></div>
<div class="abs brand"><span class="brand-mark"></span>Tidewell</div>
<div class="abs tagline">Engaged discussions about energy &amp; environment venture capital</div>

<div class="abs social-top" aria-label="Social links"><span></span><span></span><span></span></div>

<ul class="abs nav">
  <li style="margin-right:26px"><span class="ico"></span>Home</li>
  <li style="margin-right:32px"><span class="ico"></span>Profiles</li>
  <li style="margin-right:30px">Resources</li>
  <li style="margin-right:30px">About</li>
  <li style="margin-right:26px">Contact</li>
  <li>Blog</li>
</ul>

<div class="abs ticker-rule"></div>
<ul class="abs regions">
  <li class="on">US</li><li>Europe</li><li>Asia</li><li>Customize</li>
</ul>

<div class="abs quotes">
  <div class="quote" style="left:4px"><b>Broad 500</b><span class="val">1,456.65</span><br><span class="dn">-5.24</span><br><span class="dn">-0.36%</span></div>
  <svg class="quote" style="left:58px;top:1px" width="112" height="42" viewBox="0 0 112 42">
    <rect x="0" y="2" width="85" height="30" fill="#eef3f9" stroke="#d5dbe3"/>
    <line x1="0" y1="5" x2="85" y2="5" stroke="#e04040" stroke-width=".6"/>
    <polyline points="0,16 6,18 10,24 14,22 20,26 26,24 32,27 38,25 44,26 50,23 56,25 62,19 68,21 74,17 80,18 85,14" fill="none" stroke="#2f6db5" stroke-width="1"/>
    <g font-size="5" fill="#666" font-family="Arimo,sans-serif">
      <text x="88" y="5">1,465</text><text x="88" y="12">1,460</text><text x="88" y="22">1,455</text><text x="88" y="31">1,450</text>
      <text x="2" y="39">10am</text><text x="26" y="39">12pm</text><text x="50" y="39">2pm</text><text x="72" y="39">4pm</text>
    </g>
  </svg>
  <div class="quote" style="left:175px"><b>Industrials</b><span class="val">13,327.13</span><br><span class="dn">-57.16</span><br><span class="dn">-0.43%</span><br>
    <svg width="38" height="6"><polyline points="0,2 8,4 16,3 24,5 32,3 38,4" fill="none" stroke="#2f6db5" stroke-width=".8"/></svg></div>
  <div class="quote" style="left:232px"><b>Tech Comp</b><span class="val">3,090.39</span><br><span class="dn">-8.42</span><br><span class="dn">-0.27%</span><br>
    <svg width="38" height="6"><polyline points="0,3 8,2 16,4 24,3 32,5 38,4" fill="none" stroke="#2f6db5" stroke-width=".8"/></svg></div>
  <div class="quote" style="left:289px"><b>EUR/USD</b><span class="val">1.3081</span><br><span class="dn">-0.00</span><br><span class="dn">-0.35%</span><br>
    <svg width="38" height="6"><polyline points="0,1 8,3 16,2 24,5 32,4 38,5" fill="none" stroke="#2f6db5" stroke-width=".8"/></svg></div>
  <div class="quote" style="left:346px"><b>10-Year Bond</b><span class="val">1.87</span><br><span class="dn">-0.03</span><br><span class="dn">-1.68%</span><br>
    <svg width="38" height="6"><polyline points="0,2 8,3 16,2 24,4 32,3 38,4" fill="none" stroke="#2f6db5" stroke-width=".8"/></svg></div>
  <div class="quote" style="left:403px"><b>Gold</b><span class="val">1,658.30</span><br><span class="upc">12.00</span><br><span class="upc">+0.73%</span></div>
  <div class="quote" style="left:460px"><b>Oil</b><span class="val">93.22</span><br><span class="upc">0.03</span><br><span class="upc">+0.03%</span></div>
  <div class="quote-bar" style="left:0;width:169px"></div>
  <div class="quote-bar" style="left:171px;width:55px"></div>
  <div class="quote-bar" style="left:228px;width:55px"></div>
  <div class="quote-bar" style="left:285px;width:55px"></div>
  <div class="quote-bar" style="left:342px;width:55px"></div>
  <div class="quote-bar up" style="left:399px;width:55px"></div>
  <div class="quote-bar up" style="left:456px;width:52px"></div>
</div>
<div class="abs more">More »</div>

<section class="card" style="left:317px;top:191px">
  <h2 style="left:22px">News Feed</h2>
  <div class="dots" style="left:220px"><i class="on"></i><i></i><i></i></div>
  <dl class="abs news">
    <dt>Jan 6, 2013</dt>
    <dd><a>Brightfold Accelerator</a> received $1,200,000 from an undisclosed investor Growth Equity</dd>
    <dt>Jan 5, 2013</dt>
    <dd><a>KM Group</a> merged with <a>Nordvik Assurance (NVA)</a> for an Undisclosed Amount<br>NVA Terra's parent company NVA and the KM Group are to merge into a new global entity, NVA KM Group, which should position it as a leading expert in the renewable energy and power sectors, among others.</dd>
    <dt>Jan 4, 2013</dt>
    <dd><a>Tessaly Wireless</a> received an Undisclosed Amount from Corvane Systems and Halvex Semiconductor</dd>
  </dl>
  <a class="card-link" style="left:203px;top:231px">View All News</a>
</section>

<section class="card" style="left:605px;top:191px">
  <h2 style="left:22px">Company of the Month</h2>
  <div class="com-photo" role="img" aria-label="Featured company building facade against blue sky"></div>
  <p class="com-text"><a>Company Name</a> received $1,200,000 from an undisclosed investor Growth EquitySource merged with for an Undisclosed Amount<br>NVA Terra's parent company NVA and the KM Group are to merge into a new global entity, NVA KM Group, which should position it as a</p>
  <a class="card-link" style="left:202px;top:231px">View Profile</a>
</section>

<section class="card" style="left:317px;top:462px">
  <h2 style="left:17px">Blog Entries</h2>
  <div class="dots" style="left:229px"><i class="on"></i><i></i><i></i></div>
  <article class="post" style="top:50px">
    <div class="post-head"><span class="av"></span>Company<small>Uploaded Image</small><span class="time">2 Minutes ago</span></div>
    <div class="post-photo" role="img" aria-label="Green seedling leaves on white" style="background:radial-gradient(circle at 60% 50%,#8cc63f,#d6ebb5 60%,#fff)"></div>
    <p class="post-body">NVA Terra's parent company NVA and the KM Group are to merge into a new global entity, NVA KM Group, which should position it as a leading expert in the</p>
    <div class="post-meta">Comments <span class="count">30</span><span class="all">View All</span></div>
  </article>
  <article class="post" style="top:144px">
    <div class="post-head"><span class="av"></span>Company<small>Uploaded Video</small><span class="time">2 Minutes ago</span></div>
    <div class="post-photo" role="img" aria-label="Video still of stacked coins with a sprout" style="background:linear-gradient(180deg,#fff 30%,#c9a46a 70%,#8a6a3a)"></div>
    <p class="post-body">NVA Terra's parent company NVA and the KM Group are to merge into a new global entity, NVA KM Group, which should position it as a leading expert in the</p>
    <div class="post-meta">Comments <span class="count">30</span><span class="all">View All</span></div>
  </article>
  <a class="card-link" style="left:229px;top:232px">View All</a>
</section>

<section class="card" style="left:605px;top:462px">
  <h2 style="left:17px">Good Reads</h2>
  <div class="dots" style="left:229px"><i class="on"></i><i></i><i></i></div>
  <article class="read" style="top:49px">
    <div class="read-photo" role="img" aria-label="Close-up of open book pages" style="background:linear-gradient(180deg,#fff 10%,#c89a62 45%,#f3ede2 70%,#a57c4c)"></div>
    <h3>Book</h3>
    <p>Lorem ipsum dolor sit amet, consectetuer adipiscing elit, sed diam nonummy nibh euismod tincidunt ut laoreet dolore magna aliquam erat volutpat. Ut wisi enim ad minim veniam, quis nostrud exerci tation ullamcorper suscipit lobortis nisl ut aliquip ex ea commodo consequat.</p>
    <a class="see">See more</a>
  </article>
  <article class="read" style="top:142px">
    <div class="read-photo" role="img" aria-label="Hand holding coins with a green sprout" style="background:linear-gradient(180deg,#fff 15%,#a7d26b 35%,#f2dcc6 60%,#c48f5e)"></div>
    <h3>Web Site</h3>
    <p>Lorem ipsum dolor sit amet, consectetuer adipiscing elit, sed diam nonummy nibh euismod tincidunt ut laoreet dolore magna aliquam erat volutpat. Ut wisi enim ad minim veniam, quis nostrud exerci tation ullamcorper suscipit lobortis nisl ut aliquip ex ea commodo consequat.</p>
    <a class="see">See more</a>
  </article>
  <a class="card-link" style="left:231px;top:232px">View All</a>
</section>

<footer class="abs footer">
  <nav class="footer-nav"><span>Home</span><span>Q7 Profiles</span><span>Forum</span><span>Advisory</span><span>About</span><span>Contact</span><span>Blog</span></nav>
  <div class="follow">Follow us</div>
  <div class="social-foot"><span></span><span></span><span></span><span></span><span></span></div>
  <div class="footer-brand"><span class="brand-mark"></span>Tidewell</div>
</footer>

</body>
</html>
```